July 2022 Industrial Manufacturer Product Expo Mexico City

We manufacture large screws and fastners for large Mining equipment, Trains, large ships, airplanes, wind turbines, and so on. We also do custom work base on the customer needs. No matter the size we can make it.
We have a Expo coming up with companies all over the world. We have to stand out we are a family own business so our customer service will be above and beyond anyone can provide. We do not have a sales force to push our products and services we provide one on one service.
Plus@!! I'm looking for anything that you designers can come up with if it was your company to put on a business card, plus i want to do a 1 or 2 sided pamphlet, and then a website. We make Speciality Bolts for large mining equipment these bolts can be 3 to 4 foot long!!! Plus fasteners, Nuts, washers, any, size, strengths, special materials, we offer more of a ono on one customer service, We are a small company, family own, but can fulfill any type of orders. We can also provide special time lines for emergency orders. "We keep the machines running we here at KRV don't believe in down time" We want to hear any slogan based on our company to stand out.
Thanks i really appreciate all your work and options that we have to pick on. Plus just a thought we could possibly want to entertain a experience Marketing internet help maybe a employment possibility. Thanks
Updates

I need 2 cards one in Spanish and English Like the steel back ground maybe send me in some bright red and blue writing Same with the Black cards Please remove the word Military The logo KRV maybe integrate a picture of a Bolt 🔩 Thank you

Still looking for I need 2 cards one in Spanish and English Like the steel back ground maybe send me in some bright red and blue writing Same with the Black cards try bright writing Please remove the word Military The logo KRV maybe integrate a picture of a Bolt 🔩 Plus will need the company to make a brochure and website next Thank you

Target Market(s)

Large Mining, Ship, Train, Green Energy, ORBA, and Government equipment. Throughout the World

Industry/Entity Type

We can Custom Manufacture any type of Fastners for Mining equipment, Trains, Ships, Green energy, Governments, or military projects. wind turbines,

Contact Information for Business Card

I attached the name and contact info that's on a card, plus the Company Logo. Would like industrial looking background with Bright Colors that will stand out!! If we can insert somewhere maybe on back that we "Custom Manufacture Any Size or Quantity Fastners for Large Mining Equipment, Trains, Ships, Green Energy Equipment or Government Projects

Font styles to use
Other font styles liked:
• You Pick, has to be bold, colorful standout, Professional looking Beable to read it.

Colors

Designer to choose colors to be used in the design.

Requirements
Must have
• Need in Spanish and English TO STANDOUT FROM THE REST OF THE EXPO!! See Business card details, Rounded corners
Nice to have
• Can i see some of the darker cards with Bright Red and Blue letters I like to see the different type of card material, heavy thickness, plastic, transparent, Metal types, Bright Colors, I saw like Raised letters like on the logo.

```html
<!DOCTYPE html>
<html lang="es">
<head>
<meta charset="utf-8">
<title>KRV – Tarjetas de presentación</title>
<link rel="stylesheet" href="https://fonts.googleapis.com/css2?family=Arimo:wght@400;700&family=Roboto+Condensed:wght@400&display=swap">
<style>
  :root {
    --backdrop: #d9dadc;
    --card-edge: #1aa3e8;
    --black-top: #1c1c1e;
    --black-bottom: #050506;
    --name-blue: #1f4fc4;
    --text-white: #f2f4f7;
    --steel-grey: #8e9196;
    --band-blue: #2e47c9;
    --blue-light: #0a97dd;
    --blue-mid: #0565c3;
    --blue-deep: #0a1f7a;
    --silver: #dfe3e8;
  }
  * { box-sizing: border-box; margin: 0; padding: 0; }
  html, body { width: 1200px; height: 800px; overflow: hidden; }
  body {
    background: var(--backdrop);
    font-family: "Arimo", Arial, sans-serif;
    display: flex;
    align-items: center;
    justify-content: center;
    gap: 48px;
  }
  .card {
    position: relative;
    width: 540px;
    height: 308px;
    border-radius: 22px;
    overflow: hidden;
    border: 2px solid var(--card-edge);
    box-shadow: 0 14px 30px rgba(0,0,0,0.28);
  }

  /* Front: black contact card */
  .card--front .mesh {
    position: absolute; inset: 0;
    background: radial-gradient(ellipse at 55% 45%, #26262a 0%, var(--black-top) 45%, var(--black-bottom) 100%);
  }
  .edge-bands {
    position: absolute; top: 0; right: 0; width: 22px; height: 118px;
    display: flex; gap: 3px; justify-content: flex-end;
  }
  .edge-bands span { display: block; height: 100%; }
  .edge-bands .band-blue { width: 4px; background: var(--band-blue); }
  .edge-bands .band-grey { width: 9px; background: var(--steel-grey); }
  .edge-bands .band-blue-2 { width: 3px; background: var(--band-blue); }

  .front-brand {
    position: absolute; left: 40px; top: 150px;
  }
  .brand-name {
    font-weight: 700;
    color: var(--silver);
    letter-spacing: 2px;
    line-height: 1;
  }
  .front-brand .brand-name { font-size: 64px; }
  .tagline {
    font-family: "Roboto Condensed", "Arial Narrow", sans-serif;
    color: var(--text-white);
    text-transform: uppercase;
    letter-spacing: 0.5px;
  }
  .front-brand .tagline { font-size: 11px; margin-top: 8px; }

  .contact {
    position: absolute; right: 46px; top: 58px;
    text-align: right;
    color: var(--text-white);
  }
  .contact .person {
    font-weight: 700; font-size: 22px; color: var(--name-blue); margin-bottom: 6px;
  }
  .contact .note { font-size: 13px; margin-bottom: 14px; }
  .contact ul { list-style: none; }
  .contact li {
    font-size: 13px; line-height: 1.6;
    display: flex; align-items: center; justify-content: flex-end; gap: 8px;
  }
  .contact li svg { width: 12px; height: 12px; flex: none; }

  /* Back: blue brand card */
  .card--back {
    background: linear-gradient(200deg, var(--blue-light) 0%, var(--blue-mid) 45%, var(--blue-deep) 100%);
  }
  .back-brand {
    position: absolute; inset: 0;
    display: flex; flex-direction: column; align-items: center; justify-content: center;
  }
  .back-brand .brand-name { font-size: 104px; letter-spacing: 6px; }
  .back-brand .tagline { font-size: 17px; margin-top: 12px; }
</style>
</head>
<body>

  <section class="card card--front" aria-label="Tarjeta frontal con datos de contacto">
    <div class="mesh" role="img" aria-label="Textura oscura de malla hexagonal metálica"></div>
    <div class="edge-bands" aria-hidden="true">
      <span class="band-blue"></span><span class="band-grey"></span><span class="band-blue-2"></span>
    </div>

    <div class="front-brand">
      <div class="brand-name">KRV</div>
      <div class="tagline">Fabricacion y distribucion de tornillos</div>
    </div>

    <div class="contact">
      <p class="person">Lic. Mariela Soto Varga</p>
      <p class="note">Cotizaciones en</p>
      <ul>
        <li>5554028817
          <svg viewBox="0 0 12 12" aria-hidden="true"><path d="M3 1 L5 3.5 L4 5 Q5 7 7 8 L8.5 7 L11 9 L9.5 11 Q5 11 2.5 8 Q0.5 5 1 2.5 Z" fill="var(--name-blue)"/></svg>
        </li>
        <li>5556304492
          <svg viewBox="0 0 12 12" aria-hidden="true"><rect x="3" y="0.5" width="6" height="11" rx="1.2" fill="none" stroke="var(--text-white)" stroke-width="1.2"/></svg>
        </li>
        <li>ventas.krv@correo.mx
          <svg viewBox="0 0 12 12" aria-hidden="true"><rect x="0.5" y="2" width="11" height="8" fill="var(--name-blue)"/><path d="M0.5 2 L6 6.5 L11.5 2" fill="none" stroke="var(--text-white)" stroke-width="1"/></svg>
        </li>
      </ul>
    </div>
  </section>

  <section class="card card--back" aria-label="Tarjeta posterior con marca">
    <div class="back-brand">
      <div class="brand-name">KRV</div>
      <div class="tagline">Fabricacion y distribucion de tornillos</div>
    </div>
  </section>

</body>
</html>
```